International oil and gas consultancy business needs a web design

Hello, I need a web design for a new oil and gas auditing consultancy business. My business undertakes contract audit assignments to review past costs of oil and gas operations (see attached Excel file for more details of the businesses services). I need the design to give the impression of a professional consultancy style of business, rather than a retail style of website. Note: this job is for LAYOUT DESIGN ONLY and not coding / development work.
The following are my key design principles:
1. BASIC DESIGN: I am after a simple and static web design. I don't want the pages busy or cluttered with too many images or detail.
2. HORIZONTAL TABS: I require a horizontal set of tabs towards the top of the screens (see Excel file) which remain in the same position on every page.
3. META TAG PLANNING: The design should allow for effective positioning of content so that key meta tag words can easily be built during the technical build stage.
4. NUMBER OF PAGES: The site will eventually have a maximum of 10 pages. Seven of the pages will reside under the tabs. Can you please present your opening submission for the first two page.
5. USE OF MY LOGO: The attached logo (JPEG file) should be used throughout the website. Please don't change the shape and colour.
6. COLOUR SCHEMES: Can you please consider any of the 3 colour schemes below:
A - dark red (to match the logo), light grey and perhaps another of your liking;
B - dark red (to match the logo), light cream and perhaps another of your liking;
C - dark red (to match the logo), white and perhaps another of your liking.
7. WORD CONTENT: I have attached an Excel file which shows the estimated word content for each page.
8. FUTURE USE OF DESIGN: I'm planning on building a Wordpress website. Can you please ensure the layout design supports this application.

Target Market(s)

oil and gas companies (small and large)

Industry/Entity Type

Oil And Gas

Font styles to use
Sans Serif

Requirements
Nice to have
• The KOR logo and business name should ideally be next to each other. Also, the logo and name should be part of the background graphics, not above it.

```html
<!DOCTYPE html>
<html lang="en">
<head>
<meta charset="utf-8">
<title>Keystone Oil Review</title>
<link rel="stylesheet" href="https://fonts.googleapis.com/css2?family=Hind:wght@400;500;600&display=swap">
<style>
:root{
  --red:#9c1c24;
  --red-light:#b8323a;
  --red-dark:#8a161d;
  --ink:#3c3c3c;
  --muted:#6a6a6a;
  --page:#fcfcfc;
  --panel:#f5f5f5;
  --footer:#3b3b3b;
  --line:#c9c9c9;
}
*{box-sizing:border-box;margin:0;padding:0}
html,body{width:943px;height:1200px;overflow:hidden}
body{background:var(--page);font-family:"Hind",Arial,sans-serif;color:var(--muted);position:relative}
.brand{position:absolute;left:40px;top:14px;color:var(--red);font-weight:500}
.brand-name{font-size:34px;line-height:36px;letter-spacing:2px;display:block;padding-left:16px}
.brand-tag{font-size:11px;line-height:14px;display:block}
.search{position:absolute;left:740px;top:35px;width:162px;height:29px;border:1px solid var(--line);background:#fff}
.search svg{position:absolute;right:10px;top:7px}
.nav{position:absolute;left:40px;top:84px;width:863px;height:40px;
  background:linear-gradient(#c13a40,var(--red-dark));border-radius:2px;display:flex}
.nav a{color:#fff;text-decoration:none;font-size:11px;line-height:40px;text-align:center;border-right:1px solid rgba(0,0,0,.22)}
.hero{position:absolute;left:40px;top:137px;width:863px;height:303px;
  background:linear-gradient(180deg,#bbb9c6 0%,#c6b3a4 45%,#a98a66 70%,#8c7a3e 100%)}
.hero h1{position:absolute;left:113px;top:95px;font-size:28px;font-weight:600;color:#3a3a3a;letter-spacing:.3px}
.hero p{position:absolute;left:113px;top:138px;width:370px;font-size:10.5px;line-height:20.5px;color:#fff}
.hero .arrow{position:absolute;top:145px}
.welcome{position:absolute;left:40px;top:487px;width:863px;height:189px;background:var(--panel);text-align:center}
.welcome h2{margin-top:12px;font-size:21px;font-weight:400;color:var(--ink)}
.welcome h2 span{color:var(--red)}
.welcome p{margin:10px auto 0;width:780px;font-size:10.5px;line-height:20.5px}
.btn{display:inline-block;background:linear-gradient(var(--red-light),var(--red-dark));color:#fff;font-size:11px;text-decoration:none;line-height:30px;height:30px;padding:0 18px}
.welcome .btn{margin-top:16px;width:88px;padding:0}
.services-head{position:absolute;left:0;top:700px;width:943px;text-align:center}
.services-head h2{font-size:21px;font-weight:400;color:var(--red)}
.services-head p{font-size:11.5px;margin-top:2px}
.card{position:absolute;top:775px;width:268px;text-align:center}
.card .photo{height:131px}
.card h3{margin-top:22px;font-size:15.5px;font-weight:400;color:var(--red)}
.card p{margin-top:8px;font-size:10.5px;line-height:20.5px}
.card .btn{margin-top:12px;width:78px;padding:0}
.footer{position:absolute;left:0;top:1125px;width:943px;height:75px;background:var(--footer);color:#fff;font-size:11px}
.footer .links{position:absolute;left:45px;top:30px}
.footer .sep{margin:0 10px}
.footer .social{position:absolute;left:798px;top:29px;display:flex;gap:5px}
.footer .social span{width:22px;height:22px;border-radius:50%;background:#eee;display:block}
</style>
</head>
<body>
<div class="brand"><span class="brand-name">KOR</span><span class="brand-tag">Keystone Oil Review</span></div>
<div class="search"><svg width="13" height="13" viewBox="0 0 13 13"><circle cx="5.5" cy="5.5" r="4" fill="none" stroke="#555" stroke-width="1.8"/><line x1="8.5" y1="8.5" x2="12" y2="12" stroke="#555" stroke-width="2"/></svg></div>
<nav class="nav">
  <a style="width:92px">Home</a><a style="width:98px">About Us</a><a style="width:97px">Services</a><a style="width:103px">Our Partners</a><a style="width:100px">Approach</a><a style="width:121px">Why Choose Us</a><a style="width:90px;border:0">Contact Us</a>
</nav>
<section class="hero" role="img" aria-label="Oil drilling rig standing on open prairie landscape at dusk">
  <h1>FEUGIAT MALO SUADA</h1>
  <p>Lorem ipsum dolor sit amet, consectetur adipisicing elit, sed do eiusmod tempor incididunt ut labore et dolore magna aliqua. Ut enim ad minim veniam, quis nostrud exercitation ullamco.</p>
  <svg class="arrow" style="left:15px" width="26" height="26" viewBox="0 0 26 26"><circle cx="13" cy="13" r="11.5" fill="none" stroke="#fff" stroke-width="2"/><path d="M19 13H8M12 8.5 7.5 13 12 17.5" fill="none" stroke="#fff" stroke-width="2"/></svg>
  <svg class="arrow" style="left:821px" width="26" height="26" viewBox="0 0 26 26"><circle cx="13" cy="13" r="11.5" fill="none" stroke="#fff" stroke-width="2"/><path d="M7 13h11M14 8.5 18.5 13 14 17.5" fill="none" stroke="#fff" stroke-width="2"/></svg>
</section>
<section class="welcome">
  <h2>Welcome to Our Website <span>Mainpage</span></h2>
  <p>Keystone Oil Review is a Perth (Australia) based firm specialising in providing quality audit services for the oil and gas industry. Our skills and knowledge of oil and gas, along with a deep understanding of business commercial needs, ensures the high quality of our services. Keystone Oil Review is a Perth (Australia) based firm specialising in providing quality audit services for the oil and gas industry.</p>
  <a class="btn">Read More</a>
</section>
<div class="services-head"><h2>Services</h2><p>Keystone Oil Review specialise in the following services</p></div>
<article class="card" style="left:46px">
  <div class="photo" role="img" aria-label="Business handshake over a desk" style="background:linear-gradient(135deg,#8ea5bd,#2f3f55 60%,#c9d3dc)"></div>
  <h3>Joint Venture Audits</h3>
  <p>Keystone Oil Review is a Perth (Australia) based firm specialising in providing quality audit services for the oil and gas industry.</p>
  <a class="btn">View More</a>
</article>
<article class="card" style="left:338px">
  <div class="photo" role="img" aria-label="Magnifying glass over financial audit figures" style="background:linear-gradient(135deg,#dfe7ef,#9fb2c4 50%,#e8edf2)"></div>
  <h3>Contract Audits</h3>
  <p>Keystone Oil Review is a Perth (Australia) based firm specialising in providing quality audit services for the oil and gas industry.</p>
  <a class="btn">View More</a>
</article>
<article class="card" style="left:630px">
  <div class="photo" role="img" aria-label="Consultants discussing in a bright office meeting" style="background:linear-gradient(135deg,#c9cfd6,#b6a48f 50%,#dfe6ee)"></div>
  <h3>Operations Audits</h3>
  <p>Keystone Oil Review is a Perth (Australia) based firm specialising in providing quality audit services for the oil and gas industry.</p>
  <a class="btn">View More</a>
</article>
<footer class="footer">
  <div class="links">Copyright c&nbsp; 2014 Keystone Oil Review<span class="sep">&nbsp;|</span>Terms and Conditions<span class="sep">&nbsp;|</span>Privacy policy</div>
  <div class="social" aria-label="Social links"><span></span><span></span><span></span><span></span></div>
</footer>
</body>
</html>
```